Hair Extension Packaging

Update 2/16 - please keep submissions coming, I have no front runners yet. Thanks.

I need some new packaging designed for hair extensions. I have enclose pictures of what other companies packaging looks like and a few pictures of some inspiration. I am looking for a packaging that will appeal to a 20's-30's year old demographic and I like things along the lines of glamor/lace/vintage/boudoir/damask inspired. I am going to leave colors up to your creativity for the sample artwork and ask for changes if needed. Id like the design to be a standout but not loud.

The working name for this hair is "Velvetta"
Additional Text that I would like on the packaging "100% Premium Virgin Remy Human Hair"

Please keep in mind that the background of the packaging will have many different colors laying over it so be mindful of what the color you chose can effect the hair color in the packaging - no red or orange which can make the hair appear very warm and clash with ashy colors.

Working dimensions for the sample are 22" long, 3" wide.

****Once I decide on the front of the packaging I will also need the back designed which will consist of similar design as the front but with hair care instructions printed on it.***** This finished product must include front and back artwork, open Photoshop files, and additional bleed room for printing. I don't want to waste anyone's time so once I get a front design I like I will work with that artist to create the back.

Please message me with any questions.
Updates

Project Deadline Extended
Reason: Finalizing final choices. Thanks for your submissions!

Target Market(s)

Women in there 20"s - 30's. High fashion, luxurious, glamour

Industry/Entity Type

Hair

Font styles to use
Serif
Script

Requirements
Must have
• Id love the product name to be in script and then mixed with regular font (see the makeup logo example I enclosed)
Should not have
• Should not be masculine. Forget the blue and green colors

```html
<!DOCTYPE html>
<html lang="en">
<head>
<meta charset="utf-8">
<title>Velvetta Hair Extension Packaging</title>
<link rel="stylesheet" href="https://fonts.googleapis.com/css2?family=Cinzel:wght@400;600&family=Pinyon+Script&display=swap">
<style>
  :root {
    --stage-top: #e9e9e9;
    --stage-mid: #fbfbfb;
    --card: #fafafa;
    --card-edge: #dedede;
    --ink: #222222;
    --wordmark: #5f5f5f;
    --plum: #3b1c42;
    --plum-soft: #4a2752;
    --pin-white: #f7f7f7;
    --pin-line: #dcdcdc;
    --cocoa: #4a2e12;
    --cocoa-line: #5c3c1c;
    --hair-root: #3a2418;
    --hair-mid: #5b3b29;
    --hair-low: #6a4530;
    --hair-tip: #c29a66;
    --gold: #c2a270;
  }
  * { box-sizing: border-box; margin: 0; padding: 0; }
  html, body { width: 1200px; height: 1012px; overflow: hidden; }
  body {
    background: linear-gradient(180deg, var(--stage-top) 0%, var(--stage-mid) 35%, var(--stage-mid) 70%, #ececec 100%);
    font-family: "Cinzel", serif;
    color: var(--ink);
    position: relative;
  }
  .package { position: absolute; top: 0; width: 225px; height: 1012px; }
  .package--plum { left: 199px; }
  .package--pinstripe { left: 488px; }
  .package--cocoa { left: 776px; }

  /* hang tab */
  .hang-tab {
    position: absolute; top: 66px; left: 0; width: 225px; height: 53px;
    background: var(--card); border: 1px solid var(--card-edge);
    box-shadow: 0 1px 3px rgba(0,0,0,.12);
  }
  .hang-tab__name {
    position: absolute; left: 8px; top: 18px;
    font-family: "Pinyon Script", cursive; font-size: 17px; color: var(--wordmark);
  }
  .hang-tab__hole {
    position: absolute; left: 97px; top: 12px; width: 32px; height: 32px;
    border-radius: 50%; background: #ededed; border: 1px solid #c9c9c9;
  }
  .hang-tab__claim {
    position: absolute; right: 9px; top: 31px; text-align: right;
    font-size: 5px; line-height: 6px; letter-spacing: .3px; font-weight: 600;
  }

  /* backdrop panels */
  .backdrop { position: absolute; left: 0; width: 225px; bottom: 0; }
  .package--plum .backdrop {
    top: 330px;
    background: radial-gradient(ellipse at 50% 40%, var(--plum-soft) 0%, var(--plum) 70%);
  }
  .package--pinstripe .backdrop {
    top: 137px; border: 1px solid var(--card-edge);
    background: repeating-linear-gradient(90deg, var(--pin-white) 0 4px, var(--pin-line) 4px 5px);
  }
  .package--cocoa .backdrop {
    top: 380px;
    background: repeating-linear-gradient(90deg, var(--cocoa) 0 3px, var(--cocoa-line) 3px 4px);
  }

  /* hair photograph area */
  .hair {
    position: absolute; left: 22px; width: 181px; top: 395px; bottom: 0;
    background: linear-gradient(180deg, var(--hair-root) 0%, var(--hair-mid) 35%, var(--hair-low) 88%, var(--hair-tip) 100%);
    -webkit-mask-image: linear-gradient(90deg, transparent 0%, #000 14%, #000 86%, transparent 100%);
            mask-image: linear-gradient(90deg, transparent 0%, #000 14%, #000 86%, transparent 100%);
  }

  /* front label */
  .front-label {
    position: absolute; left: 0; width: 225px; background: var(--card);
    box-shadow: 0 3px 6px rgba(0,0,0,.18);
  }
  .package--plum .front-label { top: 139px; height: 262px; border-radius: 0 0 40px 40px; }
  .package--pinstripe .front-label { top: 137px; height: 262px; border-radius: 0 0 112px 112px / 0 0 62px 62px; }
  .package--cocoa .front-label { top: 134px; height: 260px; box-shadow: 0 2px 4px rgba(0,0,0,.15); }

  .logo-frame { position: absolute; display: flex; align-items: center; justify-content: center; }
  .logo-frame svg { position: absolute; inset: 0; width: 100%; height: 100%; }
  .package--plum .logo-frame { left: 9px; top: 53px; width: 206px; height: 113px; }
  .package--pinstripe .logo-frame { left: 13px; top: 55px; width: 200px; height: 105px; }
  .package--cocoa .logo-frame { left: 8px; top: 40px; width: 209px; height: 130px; }

  .brand-name {
    position: relative; font-family: "Pinyon Script", cursive; font-weight: 400;
    color: var(--wordmark); font-size: 48px; line-height: 1; padding-top: 4px;
  }
  .package--cocoa .brand-name { font-size: 60px; padding-top: 10px; }

  .claim { position: absolute; left: 0; right: 0; text-align: center; }
  .claim__top { font-size: 10px; font-weight: 600; letter-spacing: 1.3px; }
  .claim__bottom { font-size: 10px; letter-spacing: 1.3px; margin-top: 6px; }
  .package--plum .claim { top: 197px; }
  .package--pinstripe .claim { top: 197px; }
  .package--cocoa .claim { top: 199px; }
  .claim-rule { width: 156px; height: 1px; background: var(--ink); margin: 3px auto -3px; }
</style>
</head>
<body>

<section class="package package--plum">
  <div class="hang-tab">
    <span class="hang-tab__name">Velvetta</span>
    <span class="hang-tab__hole"></span>
    <span class="hang-tab__claim">100% Premium<br>Virgin Remy Human Hair</span>
  </div>
  <div class="backdrop" role="img" aria-label="Plum damask pattern panel"></div>
  <div class="hair" role="img" aria-label="Photograph of straight brown ombre hair extension"></div>
  <div class="front-label">
    <div class="logo-frame">
      <svg viewBox="0 0 206 113" aria-hidden="true">
        <rect x="3" y="4" width="200" height="105" rx="20" fill="none" stroke="var(--gold)" stroke-width="3"/>
        <rect x="10" y="11" width="186" height="91" rx="15" fill="none" stroke="#555" stroke-width="1"/>
      </svg>
      <span class="brand-name">Velvetta</span>
    </div>
    <div class="claim">
      <div class="claim__top">100% Premium</div>
      <div class="claim-rule"></div>
      <div class="claim__bottom">Virgin Remy Human Hair</div>
    </div>
  </div>
</section>

<section class="package package--pinstripe">
  <div class="hang-tab">
    <span class="hang-tab__name">Velvetta</span>
    <span class="hang-tab__hole"></span>
    <span class="hang-tab__claim">100% Premium<br>Virgin Remy Human Hair</span>
  </div>
  <div class="backdrop" role="img" aria-label="White pinstripe panel"></div>
  <div class="hair" role="img" aria-label="Photograph of straight brown ombre hair extension"></div>
  <div class="front-label">
    <div class="logo-frame">
      <svg viewBox="0 0 200 105" aria-hidden="true">
        <rect x="3" y="4" width="194" height="97" rx="22" fill="none" stroke="#1a1a1a" stroke-width="2"/>
      </svg>
      <span class="brand-name">Velvetta</span>
    </div>
    <div class="claim">
      <div class="claim__top">100% Premium</div>
      <div class="claim__bottom">Virgin Remy Human Hair</div>
    </div>
  </div>
</section>

<section class="package package--cocoa">
  <div class="hang-tab">
    <span class="hang-tab__name">Velvetta</span>
    <span class="hang-tab__hole"></span>
    <span class="hang-tab__claim">100% Premium<br>Virgin Remy Human Hair</span>
  </div>
  <div class="backdrop" role="img" aria-label="Cocoa brown pinstripe panel"></div>
  <div class="hair" role="img" aria-label="Photograph of straight brown ombre hair extension"></div>
  <div class="front-label">
    <div class="logo-frame">
      <svg viewBox="0 0 209 130" aria-hidden="true">
        <line x1="26" y1="8" x2="92" y2="8" stroke="#333" stroke-width="1.5"/>
        <circle cx="104.5" cy="8" r="4" fill="none" stroke="#999" stroke-width="1"/>
        <line x1="117" y1="8" x2="183" y2="8" stroke="#333" stroke-width="1.5"/>
        <line x1="3" y1="126" x2="206" y2="126" stroke="#333" stroke-width="1.5"/>
      </svg>
      <span class="brand-name">Velvetta</span>
    </div>
    <div class="claim">
      <div class="claim__top">100% Premium</div>
      <div class="claim__bottom">Virgin Remy Human Hair</div>
    </div>
  </div>
</section>

</body>
</html>
```